Hound Ridge Detection Services

We seek a website that will attract our customer base ( School Districts, Private, Charter Schools, Rehabilitation Centers, and Presidential Customers ( parents). The website should describe it's viewers with written and visual examples and examples of the K9 Detection Services we provide. In addition, we would like to have an educational section on the website to post ant-drug and vape materials for our client schools and parents. Lastly, a "how to contact us" with social media links, email, and phone number.
Updates

In addition to the development of a website, I will need to incorporate a business email to the domain name.

Target Market(s)

Public School Districts, Private Schools, Charter Schools, Residential ( Parents), and Rehabilitation Centers

Industry/Entity Type

K9 Detection

Coding

Coded - Design and coding required

Number of Pages Required

2 page

Font styles to use
Sans Serif

Colors
0054AA
0677BA
7BADD7
CADEEF
E8F1F8

Requirements
Must have
• Explanation/Examples of Services( Written, Pictures,Videos), Levels of Service Plans, Testimonials, Contact Information
Nice to have
• Educational Section, FAQs,
Should not have
• I can't think of anything.

```html
<!DOCTYPE html>
<html lang="en">
<head>
<meta charset="utf-8">
<title>Hound Ridge Detection Services</title>
<link rel="stylesheet" href="https://fonts.googleapis.com/css2?family=Open+Sans:wght@400;600;700&family=Tinos:wght@700&display=swap">
<style>
:root{
  --navy:#101a3d;
  --navy-deep:#0c1433;
  --blue:#0054AA;
  --blue-mid:#0677BA;
  --blue-soft:#7BADD7;
  --blue-pale:#CADEEF;
  --blue-mist:#E8F1F8;
  --cream:#f6f5f0;
  --ink:#1c2440;
  --grey:#7a7f8c;
  --white:#ffffff;
  --serif:'Tinos', 'Times New Roman', serif;
  --sans:'Open Sans', Arial, sans-serif;
}
*{margin:0;padding:0;box-sizing:border-box}
html,body{width:1200px;height:4066px;overflow:hidden}
body{position:relative;background:var(--white);font-family:var(--sans);color:var(--ink)}
.abs{position:absolute}
.eyebrow{position:absolute;left:0;width:1200px;text-align:center;font-size:14px;color:var(--blue);letter-spacing:.3px}
.eyebrow span{display:inline-block;border-bottom:2px solid var(--blue);padding:0 4px 3px}
.section-title{position:absolute;left:0;width:1200px;text-align:center;font-family:var(--serif);font-weight:700;font-size:44px;color:var(--navy)}
.btn{position:absolute;display:flex;align-items:center;justify-content:center;gap:14px;font-weight:700;font-size:15px;color:var(--white);border-radius:4px}

/* top bar */
.topbar{left:380px;top:0;width:820px;height:32px}
.topbar-text{position:absolute;top:0;height:32px;display:flex;align-items:center;gap:8px;font-size:11px;font-weight:700;color:var(--white)}

/* nav */
.brand{left:110px;top:17px;display:flex;align-items:center;gap:12px}
.brand-mark{width:70px;height:70px;border-radius:50%;background:var(--navy);border:3px solid var(--blue-pale)}
.brand-name{font-size:13px;font-weight:700;color:var(--navy);line-height:1.3;width:140px}
.nav a{position:absolute;top:60px;font-size:12px;font-weight:600;color:var(--ink);text-decoration:none}
.nav-cta{left:932px;top:54px;width:118px;height:30px;border:2px solid var(--ink);border-radius:4px;font-size:11px;font-weight:700;display:flex;align-items:center;justify-content:center}

/* hero */
.hero{left:0;top:102px;width:1200px;height:672px}
.hero-kicker{left:104px;top:284px;font-family:var(--serif);font-weight:700;font-size:20px;letter-spacing:6px;color:var(--navy)}
.hero-title{left:98px;top:300px;font-family:var(--serif);font-weight:700;font-size:72px;color:var(--navy)}
.hero-rule{left:104px;top:408px;width:494px;height:3px;background:var(--blue)}
.hero-copy{left:104px;top:428px;width:510px;font-size:16px;line-height:28px;color:var(--ink)}

/* about */
.about-photo{left:122px;top:977px;width:497px;height:341px;border-radius:4px;background:linear-gradient(135deg,#6f9a3c 0%,#4f7a28 45%,#3c4a2a 70%,#8a6a48 100%)}
.about-card{left:568px;top:1017px;width:510px;height:281px;background:var(--cream);border-radius:4px;padding:38px 28px 0 28px}
.about-card h3{font-family:var(--serif);font-weight:700;font-size:25px;color:var(--navy);margin-bottom:14px}
.about-card p{font-size:13px;line-height:17px;color:var(--grey)}

/* services */
.services{left:0;top:1410px;width:1200px;height:576px;background:linear-gradient(180deg,rgba(16,26,61,.96),rgba(24,38,82,.92)),linear-gradient(90deg,#2a3656,#46506a)}
.svc-bg{left:0;top:1410px;width:1200px;height:576px;background:radial-gradient(ellipse at 15% 70%,rgba(90,100,130,.35),transparent 50%),radial-gradient(ellipse at 85% 70%,rgba(90,100,130,.3),transparent 45%)}
.svc-eyebrow{color:var(--white)}
.svc-eyebrow span{border-color:var(--white)}
.svc-title{color:var(--white)}
.svc-card{position:absolute;top:1618px;width:304px;height:228px;overflow:hidden}
.svc-card .img{position:absolute;inset:0}
.svc-card .shade{position:absolute;left:0;right:0;bottom:0;height:110px;background:linear-gradient(180deg,transparent,rgba(10,16,40,.9))}
.svc-card h4{position:absolute;font-family:var(--serif);font-weight:700;font-size:16px;color:var(--white)}
.svc-card p{position:absolute;font-size:13px;color:var(--white);line-height:20px}
.svc-card.active .img{background:linear-gradient(135deg,#3f7fc4,#2f6db3)}
.svc-card.active .tint{position:absolute;inset:0;background:rgba(6,119,186,.75)}

/* steps */
.steps{left:0;top:1986px;width:1200px;height:482px;background:var(--blue-mist)}
.step-title{position:absolute;width:260px;text-align:center;font-family:var(--serif);font-weight:700;font-size:18px;color:var(--navy)}
.step-copy{position:absolute;width:260px;text-align:center;font-size:13px;line-height:20px;color:var(--grey)}

/* precision */
.precision{left:0;top:2468px;width:1200px;height:537px;background:var(--navy-deep)}
.precision-photo{left:0;top:2468px;width:760px;height:537px;clip-path:polygon(0 0,380px 0,520px 100%,0 100%);background:linear-gradient(160deg,#c9a36a 0%,#8d6a3e 40%,#3d3530 75%,#1b1c2a 100%)}
.precision-photo2{left:380px;top:2468px;width:380px;height:537px;clip-path:polygon(0 0,100% 0,100% 100%,140px 100%);background:linear-gradient(180deg,#2a3350,#1a2240)}
.p-eyebrow{left:632px;top:2552px;font-size:13px;color:var(--blue-mid)}
.p-title{left:632px;top:2582px;width:520px;font-family:var(--serif);font-weight:700;font-size:44px;line-height:52px;color:var(--white)}
.feature{position:absolute;left:632px;display:flex;align-items:center;gap:16px}
.feature-icon{width:62px;height:62px;border-radius:50%;background:var(--white);display:flex;align-items:center;justify-content:center}
.feature h5{font-family:var(--serif);font-weight:700;font-size:19px;color:var(--white);margin-bottom:6px}
.feature p{font-size:13px;color:var(--white)}

/* testimonials */
.avatar{position:absolute;border-radius:50%;background:linear-gradient(135deg,#d9dde4,#a9b0bd)}
.quote-badge{left:589px;top:3193px;width:60px;height:60px;border-radius:50%;background:var(--blue);display:flex;align-items:center;justify-content:center;color:var(--white);font-family:var(--serif);font-weight:700;font-size:40px;line-height:1}
.review{left:320px;top:3270px;width:560px;text-align:center;font-size:15px;line-height:23px;color:var(--grey)}
.reviewer{left:0;top:3372px;width:1200px;text-align:center;font-size:13px;color:var(--grey)}
.reviewer small{display:block;font-size:11px;margin-top:4px}
.arrow-btn{position:absolute;top:3433px;width:44px;height:44px;border-radius:50%;background:var(--navy);display:flex;align-items:center;justify-content:center}

/* footer */
.footer{left:0;top:3570px;width:1200px;height:496px}
.footer-mark{left:573px;top:3711px;width:88px;height:88px;border-radius:50%;background:var(--navy);border:3px solid var(--blue-pale)}
.footer-nav a{position:absolute;top:3827px;font-size:14px;font-weight:600;color:var(--white);text-decoration:none;transform:translateX(-50%)}
.footer-rule{left:140px;top:3878px;width:918px;height:1px;background:rgba(255,255,255,.6)}
.contact-item{position:absolute;top:3924px;display:flex;align-items:center;gap:14px;color:var(--white);font-size:12px;line-height:18px}
.contact-icon{width:56px;height:56px;border-radius:50%;border:1.5px solid var(--white);display:flex;align-items:center;justify-content:center}
.contact-item b{font-size:14px;font-weight:600}
.contact-sep{position:absolute;top:3920px;width:1px;height:64px;background:rgba(255,255,255,.7)}
.bottombar{left:0;top:4012px;width:1200px;height:54px;background:var(--blue)}
.bottombar-name{left:147px;top:4030px;font-size:13px;font-weight:600;color:var(--white)}
.social{position:absolute;top:4026px;width:26px;height:26px;border:1.5px solid var(--white);border-radius:3px}
</style>
</head>
<body>

<!-- top bar -->
<svg class="abs topbar" width="820" height="32" viewBox="0 0 820 32">
  <polygon points="30,0 820,0 820,32 0,32" fill="var(--navy)"/>
  <rect x="214" y="0" width="221" height="32" fill="var(--blue)"/>
</svg>
<div class="topbar-text" style="left:446px">
  <svg width="14" height="14" viewBox="0 0 24 24" fill="none" stroke="#fff" stroke-width="2"><path d="M5 3h4l2 5-3 2a11 11 0 0 0 6 6l2-3 5 2v4a2 2 0 0 1-2 2A17 17 0 0 1 3 5a2 2 0 0 1 2-2z"/></svg>
  512 - 555 - 0148
</div>
<div class="topbar-text" style="left:626px">
  <svg width="16" height="14" viewBox="0 0 24 20" fill="none" stroke="#fff" stroke-width="2"><rect x="2" y="2" width="20" height="16" rx="2"/><path d="M2 4l10 7 10-7"/></svg>
  REQUEST AN APPOINTMENT
</div>
<div class="topbar-text" style="left:858px">
  <svg width="12" height="14" viewBox="0 0 20 24" fill="none" stroke="#fff" stroke-width="2"><path d="M10 22s8-7 8-13a8 8 0 0 0-16 0c0 6 8 13 8 13z"/><circle cx="10" cy="9" r="3"/></svg>
  1234 Some PLace Somewhere
</div>

<!-- nav -->
<div class="abs brand">
  <div class="brand-mark"></div>
  <div class="brand-name">Hound Ridge<br>Detection Services</div>
</div>
<nav class="nav">
  <a style="left:396px">Home</a>
  <a style="left:472px">About Us</a>
  <a style="left:546px">Services</a>
  <a style="left:622px">Our Team</a>
  <a style="left:707px">Contact Us</a>
</nav>
<div class="abs nav-cta">CONTACT US</div>

<!-- hero -->
<svg class="abs hero" width="1200" height="672" viewBox="0 0 1200 672" role="img" aria-label="Two security officers with a German Shepherd detection dog standing outside an industrial building">
  <defs>
    <linearGradient id="heroPhoto" x1="0" y1="0" x2="1" y2="0">
      <stop offset="0" stop-color="#f2f4f7"/>
      <stop offset="0.35" stop-color="#e4e8ee"/>
      <stop offset="0.6" stop-color="#7a8aa6"/>
      <stop offset="0.85" stop-color="#aab2bb"/>
      <stop offset="1" stop-color="#c3c8cc"/>
    </linearGradient>
    <linearGradient id="heroGround" x1="0" y1="0" x2="0" y2="1">
      <stop offset="0" stop-color="#ffffff" stop-opacity="0"/>
      <stop offset="1" stop-color="#b6b0a4" stop-opacity=".6"/>
    </linearGradient>
  </defs>
  <rect width="1200" height="672" fill="url(#heroPhoto)"/>
  <rect y="300" width="1200" height="372" fill="url(#heroGround)"/>
  <path d="M0 628 C200 570 420 580 640 605 C860 630 1020 650 1200 600 L1200 672 L0 672 Z" fill="#fff"/>
  <path d="M0 628 C200 580 420 592 640 612 C860 632 1000 655 1200 602" fill="none" stroke="var(--blue)" stroke-width="4"/>
  <path d="M560 620 C800 660 1000 680 1200 600 L1200 630 C1020 690 820 690 560 620 Z" fill="var(--blue)"/>
</svg>
<div class="abs hero-kicker">EXPERTS IN</div>
<div class="abs hero-title">K9 Detection</div>
<div class="abs hero-rule"></div>
<p class="abs hero-copy">Lorem ipsum dolor sit amet, consectetur adipiscing elit, sed do ei usmod tempor incididunt ut lab</p>
<div class="btn" style="left:104px;top:516px;width:146px;height:40px;background:var(--blue);border-radius:20px;font-size:14px">LEARN MORE</div>
<div class="btn" style="left:260px;top:516px;width:181px;height:40px;background:var(--navy);border-radius:20px;font-size:14px">REQUEST QUOTE</div>

<!-- about -->
<div class="eyebrow" style="top:846px"><span>ABOUT US</span></div>
<h2 class="section-title" style="top:880px">Who We Are</h2>
<div class="abs about-photo" role="img" aria-label="Handler kneeling beside a German Shepherd wearing a security harness on grass"></div>
<div class="abs about-card">
  <h3>Sniffing Out Trouble Before It Strikes</h3>
  <p>Lorem ipsum dolor sit amet, consectetur adipiscing elit, sed do eiusmod tempor incididunt ut labore et dolore magna aliqua. Ut enim ad minim veniam, quis nostrud exercitation ullamco laboris nisi ut aliquip ex ea commodo consequat. Duis aute irure dolor in reprehenderit in voluptate velit esse cillum dolore eu fugiat nulla pariatur. Excepteur sint occaecat cupidatat</p>
</div>
<div class="btn" style="left:595px;top:1220px;width:157px;height:45px;background:var(--blue)">Contact us
  <svg width="18" height="14" viewBox="0 0 18 14" fill="none" stroke="#fff" stroke-width="2"><path d="M1 7h15M10 1l6 6-6 6"/></svg>
</div>

<!-- services -->
<div class="abs services" role="img" aria-label="Dim background of patrol vehicles at night"></div>
<div class="abs svc-bg"></div>
<div class="eyebrow svc-eyebrow" style="top:1487px"><span>OUR SERVICES</span></div>
<h2 class="section-title svc-title" style="top:1522px">Services We Offer</h2>

<div class="svc-card active" style="left:140px">
  <div class="img" role="img" aria-label="Officers walking a detection dog through a hallway"></div>
  <div class="tint"></div>
  <h4 style="left:0;width:304px;text-align:center;top:76px">Narcotics Detection</h4>
  <p style="left:40px;width:224px;text-align:center;top:104px">Lorem ipsum dolor sit amet, con sectetur adipiscing elit, sed do eiusmod tempor</p>
  <svg style="position:absolute;left:133px;top:174px" width="38" height="14" viewBox="0 0 38 14" fill="none" stroke="#fff" stroke-width="1.6"><path d="M1 7h35M30 1l6 6-6 6"/></svg>
</div>
<div class="svc-card" style="left:467px">
  <div class="img" role="img" aria-label="Two handlers with a detection dog beside parked vehicles" style="background:linear-gradient(160deg,#9aa3ab 0%,#6f767c 45%,#2b2f38 100%)"></div>
  <div class="shade"></div>
  <svg style="position:absolute;left:34px;top:168px" width="28" height="28" viewBox="0 0 28 28" fill="none" stroke="var(--blue-soft)" stroke-width="2"><path d="M4 24h20M8 24l6-12 6 12M14 12V4"/><circle cx="14" cy="4" r="2"/></svg>
  <h4 style="left:84px;top:162px">Contraband Detection</h4>
  <p style="left:84px;top:190px">Lorem ipsum dolor sit amet</p>
</div>
<div class="svc-card" style="left:794px">
  <div class="img" role="img" aria-label="Handler and detection dog inspecting a van" style="background:linear-gradient(160deg,#c4c2bd 0%,#8a7d6a 45%,#2b2d36 100%)"></div>
  <div class="shade"></div>
  <svg style="position:absolute;left:34px;top:168px" width="28" height="28" viewBox="0 0 28 28" fill="none" stroke="var(--blue-soft)" stroke-width="2"><path d="M4 24h20M8 24l6-12 6 12M14 12V4"/><circle cx="14" cy="4" r="2"/></svg>
  <h4 style="left:84px;top:162px">Explosives Detection</h4>
  <p style="left:84px;top:190px">Lorem ipsum dolor sit amet</p>
</div>
<div class="btn" style="left:542px;top:1893px;width:154px;height:44px;background:var(--blue)">Contact us
  <svg width="18" height="14" viewBox="0 0 18 14" fill="none" stroke="#fff" stroke-width="2"><path d="M1 7h15M10 1l6 6-6 6"/></svg>
</div>

<!-- steps -->
<div class="abs steps"></div>
<div class="eyebrow" style="top:2044px"><span>STEPS</span></div>
<h2 class="section-title" style="top:2078px">Simple Steps</h2>
<svg class="abs" style="left:0;top:2170px" width="1200" height="140" viewBox="0 0 1200 140">
  <line x1="360" y1="69" x2="559" y2="69" stroke="var(--blue)" stroke-width="2"/>
  <line x1="675" y1="69" x2="874" y2="69" stroke="var(--blue)" stroke-width="2"/>
  <g id="step1">
    <circle cx="302" cy="69" r="58" fill="#fff" stroke="var(--blue)" stroke-width="2"/>
    <circle cx="302" cy="69" r="48" fill="var(--navy)"/>
    <path d="M286 86h32M292 86l8-16 8 16M300 70l6-14" fill="none" stroke="#fff" stroke-width="2.4" stroke-linecap="round"/>
    <circle cx="356" cy="69" r="12" fill="var(--blue)" stroke="#fff" stroke-width="2"/>
    <text x="356" y="73" text-anchor="middle" font-family="Open Sans, sans-serif" font-weight="700" font-size="11" fill="#fff">01</text>
  </g>
  <g>
    <circle cx="617" cy="69" r="58" fill="#fff" stroke="var(--blue)" stroke-width="2"/>
    <circle cx="617" cy="69" r="48" fill="var(--navy)"/>
    <path d="M601 86h32M607 86l8-16 8 16M615 70l6-14" fill="none" stroke="#fff" stroke-width="2.4" stroke-linecap="round"/>
    <circle cx="671" cy="69" r="12" fill="var(--blue)" stroke="#fff" stroke-width="2"/>
    <text x="671" y="73" text-anchor="middle" font-family="Open Sans, sans-serif" font-weight="700" font-size="11" fill="#fff">01</text>
  </g>
  <g>
    <circle cx="932" cy="69" r="58" fill="#fff" stroke="var(--blue)" stroke-width="2"/>
    <circle cx="932" cy="69" r="48" fill="var(--navy)"/>
    <path d="M916 86h32M922 86l8-16 8 16M930 70l6-14" fill="none" stroke="#fff" stroke-width="2.4" stroke-linecap="round"/>
    <circle cx="986" cy="69" r="12" fill="var(--blue)" stroke="#fff" stroke-width="2"/>
    <text x="986" y="73" text-anchor="middle" font-family="Open Sans, sans-serif" font-weight="700" font-size="11" fill="#fff">01</text>
  </g>
</svg>
<div class="step-title" style="left:172px;top:2314px">Contact Us to Start</div>
<div class="step-title" style="left:487px;top:2314px">Set Up an Appointment</div>
<div class="step-title" style="left:802px;top:2314px">Get Assigned an Expert</div>
<p class="step-copy" style="left:172px;top:2343px">Lorem ipsum dolor sit amet, consectetur adipiscing elit, sed do eiusmod</p>
<p class="step-copy" style="left:487px;top:2343px">Lorem ipsum dolor sit amet, consectetur adipiscing elit, sed do eiusmod</p>
<p class="step-copy" style="left:802px;top:2343px">Lorem ipsum dolor sit amet, consectetur adipiscing elit, sed do eiusmod</p>

<!-- precision -->
<div class="abs precision"></div>
<div class="abs precision-photo2"></div>
<div class="abs precision-photo" role="img" aria-label="Handler leading a detection dog through a school classroom"></div>
<div class="abs p-eyebrow">WHO WE ARE</div>
<h2 class="abs p-title">Precision Paws for a Safer Tomorrow</h2>
<div class="feature" style="top:2720px">
  <div class="feature-icon"><svg width="32" height="32" viewBox="0 0 32 32" fill="none" stroke="var(--blue)" stroke-width="2"><path d="M16 3l4 5 6 1-1 6 3 5-6 2-2 6-4-3-4 3-2-6-6-2 3-5-1-6 6-1z"/></svg></div>
  <div><h5>On-Time Appointments</h5><p>Lorem ipsum dolor sit amet, consectetur sipid</p></div>
</div>
<div class="feature" style="top:2803px">
  <div class="feature-icon"><svg width="32" height="32" viewBox="0 0 32 32" fill="none" stroke="var(--blue)" stroke-width="2"><path d="M16 3l4 5 6 1-1 6 3 5-6 2-2 6-4-3-4 3-2-6-6-2 3-5-1-6 6-1z"/></svg></div>
  <div><h5>Client Centric</h5><p>Lorem ipsum dolor sit amet, consectetur sipid</p></div>
</div>
<div class="feature" style="top:2887px">
  <div class="feature-icon"><svg width="32" height="32" viewBox="0 0 32 32" fill="none" stroke="var(--blue)" stroke-width="2"><path d="M16 3l4 5 6 1-1 6 3 5-6 2-2 6-4-3-4 3-2-6-6-2 3-5-1-6 6-1z"/></svg></div>
  <div><h5>Experienced Professionals</h5><p>Lorem ipsum dolor sit amet, consectetur sipid</p></div>
</div>

<!-- testimonials -->
<div class="eyebrow" style="top:3059px"><span>TESTIMONIALS</span></div>
<h2 class="section-title" style="top:3093px">Client Reviews</h2>
<div class="avatar" role="img" aria-label="Client portrait" style="left:240px;top:3193px;width:60px;height:60px"></div>
<div class="avatar" role="img" aria-label="Client portrait" style="left:91px;top:3250px;width:100px;height:100px;background:linear-gradient(135deg,#b89a7c,#6a5444)"></div>
<div class="avatar" role="img" aria-label="Client portrait" style="left:261px;top:3310px;width:40px;height:40px"></div>
<div class="avatar" role="img" aria-label="Client portrait" style="left:171px;top:3384px;width:84px;height:84px;background:linear-gradient(135deg,#e6dcd2,#b9a796)"></div>
<div class="avatar" role="img" aria-label="Client portrait" style="left:892px;top:3179px;width:50px;height:50px;background:linear-gradient(135deg,#9aa0a6,#4e545c)"></div>
<div class="avatar" role="img" aria-label="Client portrait" style="left:1003px;top:3237px;width:104px;height:104px"></div>
<div class="avatar" role="img" aria-label="Client portrait" style="left:872px;top:3352px;width:60px;height:60px;background:linear-gradient(135deg,#f2cf9a,#e0a860)"></div>
<div class="avatar" role="img" aria-label="Client portrait" style="left:997px;top:3390px;width:80px;height:80px;background:linear-gradient(135deg,#eef0ee,#b8c2a8)"></div>
<div class="abs quote-badge">&#8221;</div>
<p class="abs review">Lorem ipsum dolor sit amet, consectetur adipiscing elit, sed do eiusmod tempor incididunt ut labore et dolore magna aliqua. Ut enim ad minim veniam, quis nostrud exercitation ullamco laboris nisi ut aliquip ex ea comm odo consequat. Duis aute irure</p>
<div class="abs reviewer">Marcus Bell<small>Client</small></div>
<div class="arrow-btn" style="left:568px"><svg width="12" height="14" viewBox="0 0 12 14" fill="none" stroke="#fff" stroke-width="2.4"><path d="M3 1l6 6-6 6"/></svg></div>
<div class="arrow-btn" style="left:622px"><svg width="12" height="14" viewBox="0 0 12 14" fill="none" stroke="#fff" stroke-width="2.4"><path d="M9 1L3 7l6 6"/></svg></div>

<!-- footer -->
<svg class="abs footer" width="1200" height="496" viewBox="0 0 1200 496">
  <path d="M0 72 C220 20 420 0 640 40 C860 80 1040 60 1200 20 L1200 496 L0 496 Z" fill="var(--blue)"/>
  <path d="M0 110 C220 50 420 30 640 66 C860 100 1040 80 1200 34 L1200 496 L0 496 Z" fill="var(--navy-deep)"/>
</svg>
<div class="abs footer-mark"></div>
<div class="abs" style="left:0;top:3803px;width:1200px;text-align:center;font-size:12px;font-weight:600;color:var(--white)">Hound Ridge Detection Services</div>
<nav class="footer-nav">
  <a style="left:374px">HOME</a>
  <a style="left:477px">SERVICES</a>
  <a style="left:586px">ABOUT US</a>
  <a style="left:720px">TESTIMONIALS</a>
  <a style="left:840px">BLOG</a>
</nav>
<div class="abs footer-rule"></div>
<div class="contact-item" style="left:172px">
  <div class="contact-icon"><svg width="30" height="30" viewBox="0 0 30 30" fill="none" stroke="#fff" stroke-width="1.6"><circle cx="15" cy="15" r="12"/><ellipse cx="15" cy="15" rx="5" ry="12"/><path d="M3 15h24M5 9h20M5 21h20"/></svg></div>
  <div>123, Building Name, Street<br>City, State XY 123456</div>
</div>
<div class="contact-sep" style="left:430px"></div>
<div class="contact-item" style="left:506px">
  <div class="contact-icon"><svg width="22" height="30" viewBox="0 0 22 30" fill="none" stroke="#fff" stroke-width="1.6"><rect x="3" y="2" width="16" height="26" rx="2"/><path d="M9 24h4"/></svg></div>
  <div><b>PHONE</b><br>(123) 456 7890</div>
</div>
<div class="contact-sep" style="left:750px"></div>
<div class="contact-item" style="left:828px">
  <div class="contact-icon"><svg width="30" height="24" viewBox="0 0 30 24" fill="none" stroke="#fff" stroke-width="1.6"><rect x="2" y="2" width="26" height="20" rx="2"/><path d="M2 4l13 9 13-9"/></svg></div>
  <div><b>EMAIL</b><br>info@company.com</div>
</div>
<div class="abs bottombar"></div>
<div class="abs bottombar-name">Hound Ridge Detection Services</div>
<div class="social" style="left:933px"></div>
<div class="social" style="left:966px"></div>
<div class="social" style="left:999px"></div>
<div class="social" style="left:1032px"></div>

</body>
</html>
```